Web development startup company needs a web design

We need a design for a company starting out, based in Australia. The business focuses on Veltrix database solutions - Veltrix database development, web development, support, etc. As such, needs a professional look and feel to it.
I'm thinking a single page design where the user can either click a nav bar to go to the relevant section in the page or scroll down is the best shot - but I'm no designer so happy with any suggestions.
I envisions three sections to the page
1. An about us:
2. Project listing
3. Contact form.
Industry/Entity Type
Business
Coding
Coded - Design and coding required
Number of Pages Required
1 page
Look and feel

```html
<!DOCTYPE html>
<html lang="en">
<head>
<meta charset="utf-8">
<title>Harbourline Data Solutions</title>
<link rel="stylesheet" href="https://fonts.googleapis.com/css2?family=Antonio:wght@200;300&family=Open+Sans:wght@400;600;700&family=Roboto+Condensed:wght@400&display=swap">
<style>
  :root {
    --cyan: #1fbde6;
    --cyan-soft: #41c6ea;
    --nav-band: #7fd6f0;
    --ink: #2e2e2e;
    --grey-text: #8a8a8a;
    --field: #ececec;
    --card-line: #e2e2e2;
    --footer: #2b2b2b;
    --white: #ffffff;
  }
  * { box-sizing: border-box; margin: 0; padding: 0; }
  html, body { width: 712px; height: 1200px; overflow: hidden; background: var(--white); }
  body { position: relative; font-family: "Open Sans", Arial, sans-serif; color: var(--ink); }
  .abs { position: absolute; }

  .hero {
    left: 0; top: 0; width: 712px; height: 340px;
    background: radial-gradient(ellipse at 72% 45%, #9fb6c4 0%, #4f7f95 30%, #2c6c80 60%, #1f5368 100%);
  }
  .hero-art {
    left: 70px; top: 60px; width: 260px; height: 260px;
    background: radial-gradient(circle at 50% 50%, #d8dde2 0%, #8a96a0 40%, rgba(40,120,170,0.3) 70%, rgba(0,0,0,0) 75%);
  }
  .hero-label { color: var(--white); font-weight: 700; font-size: 13px; }
  .brand {
    left: 263px; top: 0; width: 186px; height: 62px; background: var(--white);
    border-radius: 0 0 4px 4px; display: flex; align-items: center; justify-content: center; gap: 8px;
  }
  .brand-dot { width: 22px; height: 22px; border-radius: 50%; background: var(--cyan); }
  .brand-name { color: var(--cyan); font-size: 15px; font-weight: 600; line-height: 1.05; }
  .headline {
    height: 31px; background: rgba(235,240,244,0.7); color: #1e1e1e;
    font-family: "Antonio", sans-serif; font-weight: 300; font-size: 20px;
    display: flex; align-items: center; justify-content: center; letter-spacing: 0.3px;
  }
  .slide-arrow {
    width: 30px; height: 30px; border-radius: 50%; background: rgba(255,255,255,0.25);
    display: flex; align-items: center; justify-content: center;
  }

  .nav { left: 0; top: 340px; width: 712px; height: 42px; background: var(--nav-band); }
  .nav-item {
    top: 350px; height: 23px; color: var(--white); font-family: "Roboto Condensed", sans-serif;
    font-size: 12px; display: flex; align-items: center; justify-content: center;
  }
  .nav-item.is-active { border: 1px solid var(--white); }

  .section-title {
    left: 0; width: 712px; text-align: center; font-family: "Antonio", sans-serif;
    font-weight: 200; color: #222; letter-spacing: 0.5px;
  }

  .service-card {
    top: 495px; width: 198px; height: 126px; background: var(--white);
    border: 1px solid var(--card-line); box-shadow: 0 1px 3px rgba(0,0,0,0.12); text-align: center;
  }
  .service-icon {
    top: 462px; width: 66px; height: 66px; border-radius: 50%; background: var(--white);
    border-top: 2px solid var(--card-line); display: flex; align-items: center; justify-content: center;
  }
  .service-title {
    margin-top: 44px; font-family: "Antonio", sans-serif; font-weight: 300;
    font-size: 16px; color: var(--cyan-soft);
  }
  .service-text { margin: 8px 12px 0; font-size: 9.5px; line-height: 15px; color: var(--grey-text); }

  .project-shot { top: 718px; width: 148px; height: 246px; border: 1px solid #e5e5e5; }
  .project-overlay {
    left: 58px; top: 934px; width: 124px; height: 61px; background: var(--cyan);
    display: flex; flex-direction: column; align-items: center; justify-content: center; gap: 6px;
  }
  .project-name { color: var(--white); font-family: "Antonio", sans-serif; font-weight: 300; font-size: 14px; }
  .project-link { color: var(--white); font-size: 9.5px; border: 1px solid var(--white); padding: 3px 10px; }
  .carousel-arrow {
    top: 822px; width: 24px; height: 24px; border-radius: 50%; border: 1px solid #d6d6d6;
    display: flex; align-items: center; justify-content: center; background: var(--white);
  }

  .field {
    height: 24px; background: var(--field); font-size: 9.5px; color: #444;
    display: flex; align-items: center; padding-left: 8px;
  }
  .send-button {
    left: 468px; top: 1107px; width: 198px; height: 24px; background: var(--cyan); color: var(--white);
    font-size: 9.5px; font-weight: 700; display: flex; align-items: center; justify-content: center;
  }

  .footer { left: 0; top: 1169px; width: 712px; height: 31px; background: var(--footer); }
  .copyright { left: 46px; top: 1178px; color: var(--white); font-size: 7.5px; font-weight: 700; }
  .social-dot { top: 1175px; width: 18px; height: 18px; border-radius: 50%; background: #6d6d6d; }
  .to-top {
    left: 673px; top: 1162px; width: 31px; height: 31px; border-radius: 50%; background: #3f8fa8;
    display: flex; align-items: center; justify-content: center;
  }
</style>
</head>
<body>
  <div class="abs hero" role="img" aria-label="Hero background: glowing network globe in teal and blue tones"></div>
  <div class="abs hero-art" role="img" aria-label="Illustration of a metallic cube with blue blocks and arrows"></div>
  <span class="abs hero-label" style="left:79px;top:97px;">Security</span>
  <span class="abs hero-label" style="left:252px;top:279px;">Availability</span>
  <span class="abs hero-label" style="left:80px;top:301px;">Performance</span>

  <div class="abs brand">
    <span class="brand-dot"></span>
    <span class="brand-name">Harbourline<br>Data Solutions</span>
  </div>

  <div class="abs headline" style="left:334px;top:140px;width:191px;">TAKE YOUR VELTRIX</div>
  <div class="abs headline" style="left:378px;top:183px;width:190px;">BUSSINESS TO</div>
  <div class="abs headline" style="left:433px;top:226px;width:191px;">THE NEXT LEVEL</div>

  <div class="abs slide-arrow" style="left:7px;top:164px;">
    <svg width="10" height="12" viewBox="0 0 10 12"><path d="M7 1 L2 6 L7 11" fill="none" stroke="#fff" stroke-width="1.6"/></svg>
  </div>
  <div class="abs slide-arrow" style="left:675px;top:164px;">
    <svg width="10" height="12" viewBox="0 0 10 12"><path d="M3 1 L8 6 L3 11" fill="none" stroke="#fff" stroke-width="1.6"/></svg>
  </div>

  <nav>
    <div class="abs nav"></div>
    <span class="abs nav-item is-active" style="left:181px;width:49px;">Home</span>
    <span class="abs nav-item" style="left:262px;width:60px;">About</span>
    <span class="abs nav-item" style="left:349px;width:70px;">Portfolio</span>
    <span class="abs nav-item" style="left:450px;width:80px;">Contact Us</span>
  </nav>

  <h2 class="abs section-title" style="top:414px;font-size:26px;">GREAT SERVICES</h2>

  <div class="abs service-card" style="left:46px;">
    <p class="service-title">LOREM IPSUM</p>
    <p class="service-text">Lorem Ipsum is simply dummy text of the printing and typesetting industry.</p>
  </div>
  <div class="abs service-card" style="left:257px;">
    <p class="service-title">LOREM IPSUM</p>
    <p class="service-text">Lorem Ipsum is simply dummy text of the printing and typesetting industry.</p>
  </div>
  <div class="abs service-card" style="left:468px;">
    <p class="service-title">LOREM IPSUM</p>
    <p class="service-text">Lorem Ipsum is simply dummy text of the printing and typesetting industry.</p>
  </div>

  <div class="abs service-icon" style="left:112px;">
    <svg width="46" height="46" viewBox="0 0 46 46">
      <circle cx="23" cy="23" r="21" fill="none" stroke="var(--cyan-soft)" stroke-width="2.5"/>
      <circle cx="23" cy="19" r="7" fill="none" stroke="var(--cyan-soft)" stroke-width="2"/>
      <path d="M19 25 L19 35 L23 32 L27 35 L27 25" fill="none" stroke="var(--cyan-soft)" stroke-width="2"/>
    </svg>
  </div>
  <div class="abs service-icon" style="left:323px;">
    <svg width="46" height="46" viewBox="0 0 46 46">
      <circle cx="23" cy="23" r="21" fill="none" stroke="#9a9a9a" stroke-width="2.5"/>
      <circle cx="19" cy="21" r="6" fill="none" stroke="#9a9a9a" stroke-width="2.5" stroke-dasharray="3 2"/>
      <circle cx="28" cy="28" r="4" fill="none" stroke="#9a9a9a" stroke-width="2.5" stroke-dasharray="2 2"/>
    </svg>
  </div>
  <div class="abs service-icon" style="left:534px;">
    <svg width="46" height="46" viewBox="0 0 46 46">
      <circle cx="23" cy="23" r="21" fill="none" stroke="#9a9a9a" stroke-width="2.5"/>
      <rect x="13" y="15" width="6" height="16" fill="#9a9a9a"/>
      <rect x="20" y="13" width="6" height="18" fill="#9a9a9a"/>
      <rect x="27" y="15" width="6" height="16" fill="#9a9a9a"/>
    </svg>
  </div>

  <h2 class="abs section-title" style="top:666px;font-size:28px;">CHECK OUT SOME OF OUR LATEST AND GREATEST PROJECTS</h2>

  <div class="abs carousel-arrow" style="left:13px;">
    <svg width="10" height="10" viewBox="0 0 10 10"><path d="M9 5 H1 M4 2 L1 5 L4 8" fill="none" stroke="#aaa" stroke-width="1.3"/></svg>
  </div>
  <div class="abs carousel-arrow" style="left:675px;">
    <svg width="10" height="10" viewBox="0 0 10 10"><path d="M1 5 H9 M6 2 L9 5 L6 8" fill="none" stroke="#aaa" stroke-width="1.3"/></svg>
  </div>

  <div class="abs project-shot" style="left:46px;background:linear-gradient(180deg,#f4f4f4 0%,#d9a86a 12%,#f6f6f6 30%,#f6f6f6 50%,#6a7880 60%,#c9a070 72%,#f4f4f4 80%);" role="img" aria-label="Project screenshot: architecture company website"></div>
  <div class="abs project-shot" style="left:204px;background:linear-gradient(180deg,#2f3338 0%,#5b646c 30%,#f3f3f3 31%,#f3f3f3 52%,#3b3f44 53%,#3b3f44 72%,#f3f3f3 73%,#f3f3f3 77%,#2f3236 78%);" role="img" aria-label="Project screenshot: car wash website"></div>
  <div class="abs project-shot" style="left:361px;background:linear-gradient(180deg,#4fc7bd 0%,#bfe6e2 18%,#f4f4f4 45%,#f4f4f4 93%,#e0506a 94%);" role="img" aria-label="Project screenshot: business solutions website"></div>
  <div class="abs project-shot" style="left:518px;background:linear-gradient(180deg,#f6f6f6 0%,#5f8f3e 6%,#4a7d2d 33%,#f4f4f4 34%,#f4f4f4 100%);" role="img" aria-label="Project screenshot: cleaning tools shop website"></div>

  <div class="abs project-overlay">
    <span class="project-name">PROJECT NAME</span>
    <span class="project-link">View Project</span>
  </div>

  <h2 class="abs section-title" style="top:1024px;font-size:24px;">CONTACT INFO</h2>

  <form>
    <div class="abs field" style="left:46px;top:1076px;width:197px;">Name</div>
    <div class="abs field" style="left:257px;top:1076px;width:197px;">E- Mail</div>
    <div class="abs field" style="left:468px;top:1076px;width:198px;">Company Name</div>
    <div class="abs field" style="left:46px;top:1107px;width:408px;">Message</div>
    <div class="abs send-button">SEND</div>
  </form>

  <footer>
    <div class="abs footer"></div>
    <p class="abs copyright">© 2015 Harbourline Data Solutions.All Rights Reserved.</p>
    <span class="abs social-dot" style="left:578px;"></span>
    <span class="abs social-dot" style="left:601px;"></span>
    <span class="abs social-dot" style="left:624px;"></span>
    <span class="abs social-dot" style="left:647px;"></span>
    <div class="abs to-top">
      <svg width="14" height="10" viewBox="0 0 14 10"><path d="M1 8 L7 2 L13 8" fill="none" stroke="#fff" stroke-width="1.6"/></svg>
    </div>
  </footer>
</body>
</html>
```